Orbit Crust gazebo signage project.

We are looking for signage for our mobile pizzeria gazebo structure. We sell pizza from a woodfired oven, Neapolitan style. We have a KD campervan which we sell pizza from too, which is yellow and black, so we would like to stick with those colours. The signage needs to be 2, 305cm x 76cm one for the top, and one for the bottom. It needs to state clearly the product is pizza. It also needs to include our logo, our website and that we sell Neapolitan style woodfired pizza. Our website is orbitcrust.co.uk to get a feel of our brand. We also don't want photos of pizza on the design.

Colors
000000
fbed22

Requirements
Must have
• The colours yellow and black and our logo on the top banner. Our website and the facebook, twitter and instagram logos on the bottom banner.

```html
<!DOCTYPE html>
<html lang="en">
<head>
<meta charset="utf-8">
<title>Orbit Crust – Gazebo Banners</title>
<link rel="stylesheet" href="https://fonts.googleapis.com/css2?family=Lobster&family=Open+Sans:wght@400;700&display=swap">
<style>
  :root {
    --sheet: #4a4a4a;
    --slate-dark: #1c1c1c;
    --slate-mid: #2f2f2f;
    --yellow: #fbd000;
    --white: #ffffff;
    --frame: #f2f2f2;
  }
  * { margin: 0; padding: 0; box-sizing: border-box; }
  html, body { width: 925px; height: 1200px; overflow: hidden; }
  body {
    background: var(--sheet);
    font-family: "Lobster", cursive;
    position: relative;
  }
  .banner-label {
    position: absolute;
    left: 0;
    width: 82px;
    text-align: center;
    font-family: "Open Sans", Arial, sans-serif;
    font-size: 15px;
    color: var(--white);
  }
  .banner {
    position: absolute;
    left: 82px;
    width: 811px;
    height: 202px;
    background: radial-gradient(ellipse at 40% 40%, var(--slate-mid), var(--slate-dark) 80%);
    border: 1px solid #222;
    overflow: hidden;
  }
  .banner-frame {
    position: absolute;
    inset: 7px;
    border: 2px solid var(--frame);
    border-radius: 12px;
    overflow: hidden;
  }
  .banner--top { top: 385px; }
  .banner--bottom { top: 613px; }

  /* top banner */
  .brand {
    position: absolute;
    left: 14px;
    top: 76px;
    display: flex;
    align-items: center;
    gap: 8px;
  }
  .brand-dot {
    width: 24px; height: 24px;
    border: 3px solid var(--white);
    border-radius: 50%;
  }
  .brand-name {
    color: var(--white);
    font-size: 27px;
    line-height: 1;
  }
  .tagline {
    position: absolute;
    left: 177px;
    top: 10px;
    color: var(--white);
    font-size: 26px;
    line-height: 1;
  }
  .product-line {
    position: absolute;
    color: var(--yellow);
    line-height: 1;
  }
  .product-line--woodfired { left: 177px; top: 48px; font-size: 56px; }
  .product-line--pizza { left: 315px; top: 108px; font-size: 74px; }
  .photo-table {
    position: absolute;
    right: 0; top: 0; bottom: 0;
    width: 290px;
    background: linear-gradient(90deg, rgba(40,40,40,0) 0%, #5a5048 25%, #b8643a 55%, #d04a2a 75%, #6a5a4c 100%);
  }

  /* bottom banner */
  .photo-oven {
    position: absolute;
    left: 0; top: 0; bottom: 0;
    width: 262px;
    background: linear-gradient(90deg, #e8702a 0%, #f0a040 40%, #a0401c 80%, rgba(40,40,40,0) 100%);
  }
  .social {
    position: absolute;
    top: 17px;
    right: 18px;
    display: flex;
    gap: 10px;
  }
  .social-dot {
    width: 26px; height: 26px;
    border-radius: 50%;
    background: var(--yellow);
  }
  .contact-prompt {
    position: absolute;
    left: 278px;
    top: 56px;
    color: var(--white);
    font-size: 31px;
    line-height: 1;
  }
  .web-address {
    position: absolute;
    left: 278px;
    top: 96px;
    color: var(--white);
    font-size: 50px;
    line-height: 1;
    white-space: nowrap;
  }
  .web-address .domain { color: var(--yellow); }
</style>
</head>
<body>
  <div class="banner-label" style="top:474px;">TOP</div>
  <section class="banner banner--top">
    <div class="banner-frame">
      <div class="brand">
        <span class="brand-dot"></span>
        <span class="brand-name">Orbit Crust</span>
      </div>
      <p class="tagline">Neapolitan style</p>
      <p class="product-line product-line--woodfired">Woodfired</p>
      <p class="product-line product-line--pizza">Pizza</p>
      <div class="photo-table" role="img" aria-label="Tomato-topped pizza with a slice cut out on a rustic wooden table with herbs and cherry tomatoes"></div>
    </div>
  </section>

  <div class="banner-label" style="top:703px;">BOTTOM</div>
  <section class="banner banner--bottom">
    <div class="banner-frame">
      <div class="photo-oven" role="img" aria-label="Pizza on a peel in front of the flames of a woodfired oven"></div>
      <div class="social" aria-label="Social media">
        <span class="social-dot"></span>
        <span class="social-dot"></span>
        <span class="social-dot"></span>
      </div>
      <p class="contact-prompt">Get in touch with us!</p>
      <p class="web-address">www.<span class="domain">orbitcrust</span>.co.uk</p>
    </div>
  </section>
</body>
</html>
```